Hello there!
I am looking to have a label created for a jojoba oil product I am launching. I have attached the logo of my company below. The label should have the following information on it as well:
Ingredients: pure jojoba oil
Size of the bottle: 118ml
And there might be more but I am working on this and will keep you posted.

```html
<!DOCTYPE html>
<html lang="en">
<head>
<meta charset="UTF-8">
<title>Meadowlark Hair Atelier – Jojoba Oil Label</title>
<link rel="stylesheet" href="https://fonts.googleapis.com/css2?family=Montserrat:wght@400;500;600;700&display=swap">
<style>
  :root {
    --page: #ffffff;
    --label-dark: #272622;
    --gold: #b8926a;
    --green: #00953f;
    --ink: #1f2a22;
  }
  * { margin: 0; padding: 0; box-sizing: border-box; }
  html, body {
    width: 1200px;
    height: 1000px;
    overflow: hidden;
    background: var(--page);
    font-family: "Montserrat", sans-serif;
  }
  .canvas {
    position: relative;
    width: 1200px;
    height: 1000px;
  }
  .label {
    position: absolute;
    left: 345px;
    top: 145px;
    width: 510px;
    height: 710px;
    border-radius: 42px;
    background: var(--label-dark);
    overflow: hidden;
    text-align: center;
  }
  .brand-name {
    position: absolute;
    left: 0;
    right: 0;
    top: 96px;
    color: var(--gold);
    font-weight: 500;
    font-size: 38px;
    line-height: 50px;
    letter-spacing: 0.08em;
    text-transform: uppercase;
  }
  .product-name {
    position: absolute;
    left: 0;
    right: 0;
    top: 285px;
    color: var(--green);
    font-weight: 700;
    font-size: 50px;
    line-height: 64px;
    letter-spacing: 0.06em;
  }
  .product-type {
    position: absolute;
    left: 0;
    right: 0;
    top: 348px;
    color: var(--gold);
    font-weight: 400;
    font-size: 17px;
    letter-spacing: 0.12em;
  }
  .volume {
    position: absolute;
    left: 0;
    right: 0;
    top: 589px;
    color: var(--gold);
    font-weight: 600;
    font-size: 28px;
  }
  .footer-band {
    position: absolute;
    left: 0;
    right: 0;
    bottom: 0;
    height: 58px;
    background: var(--green);
    display: flex;
    align-items: center;
    justify-content: center;
    gap: 12px;
    color: var(--ink);
    font-weight: 700;
    font-size: 15px;
    letter-spacing: 0.08em;
  }
</style>
</head>
<body>
  <div class="canvas">
    <section class="label">
      <h1 class="brand-name">Meadowlark<br>Hair Atelier</h1>
      <h2 class="product-name">JOJOBA OIL</h2>
      <p class="product-type">PURE CARRIER OIL</p>
      <p class="volume">118ml</p>
      <div class="footer-band">
        <span>PURE CARRIER OIL</span>
        <span>PURE CARRIER OIL</span>
      </div>
    </section>
  </div>
</body>
</html>
```